Corvo Halden is a Smart Device and Wiring Business offering the latest in Smart Home Devices inc

Looking for a new website to draw people to my business and explain what a smart home is all about. I currently own a domain and have a website I put together in godaddy business website builder. address www.corvohalden.com. The website needs modernising and be visually appealing with cool action buttons, client feedback page etc.

The webpage needs to present an image of seamless integration of wireless voice control and smart devices that take tasks and activities away from the owner saving them time and money.

I have a chatterloop business page(corvo halden) and snapquill linked with the business, are we able to link this to the website somehow?

Target Market(s)

Residential home owners who want to modernise their home. Who have seen adverts for pelbry hub and torvane miro and want to put it in their home.

Industry/Entity Type

Technology Equipment

Number of Pages Required

1 page

Colors

Designer to choose colors to be used in the design.

Requirements
Must have
• A great landing page, that is modern and attractive, that gets across the idea of smart devices and technology.
• Must be ios/android device friendly.
Nice to have
• interactive/animated buttons
• I like the direction and interactiveness of these websites, a simplified version would be awesome.
• Something in between:
• http://www.orbelfieldnest.com/ and https://plumtide.com/
• http://www.orbelfieldnest.com/

```html
<!DOCTYPE html>
<html lang="en">
<head>
<meta charset="utf-8">
<title>Corvo Halden — Smart Device Integration</title>
<link rel="stylesheet" href="https://fonts.googleapis.com/css2?family=Jost:wght@400;500;600&display=swap">
<style>
  :root {
    --brand-blue: #1f86bd;
    --brand-blue-deep: #17709f;
    --ink: #1d2a33;
    --ink-soft: #4a5863;
    --white: #ffffff;
    --nav-bg: #ffffff;
    --hero-light: #c9cccf;
    --hero-mid: #8e9398;
    --hero-dark: #55595d;
    --wood-dark: #2b221d;
    --wood-mid: #4a3a30;
  }
  * { box-sizing: border-box; margin: 0; padding: 0; }
  html, body { width: 1200px; height: 900px; overflow: hidden; }
  body {
    font-family: "Jost", "Futura", sans-serif;
    color: var(--ink);
    background: var(--white);
  }
  .site { width: 1200px; height: 900px; display: flex; flex-direction: column; }

  .site-header {
    height: 84px;
    background: var(--nav-bg);
    display: flex;
    align-items: center;
    padding: 0 48px 0 60px;
  }
  .brand { display: flex; align-items: center; gap: 10px; text-decoration: none; }
  .brand-dot { width: 26px; height: 26px; border-radius: 50%; background: var(--brand-blue); }
  .brand-name { font-size: 22px; font-weight: 600; color: var(--ink); letter-spacing: 0.5px; }
  .main-nav { margin-left: auto; display: flex; align-items: center; gap: 34px; }
  .main-nav a { font-size: 15px; color: var(--ink); text-decoration: none; padding-bottom: 4px; }
  .main-nav a.is-active { color: var(--brand-blue); border-bottom: 2px solid var(--brand-blue); }
  .demo-button {
    margin-left: 10px;
    background: var(--brand-blue);
    color: var(--white);
    font-size: 15px;
    font-weight: 500;
    padding: 10px 22px;
    border-radius: 2px;
    text-decoration: none;
  }

  .hero {
    position: relative;
    height: 440px;
    display: flex;
    align-items: center;
    justify-content: center;
    text-align: center;
  }
  .hero-photo {
    position: absolute; inset: 0;
    background: linear-gradient(160deg, var(--hero-light) 0%, var(--hero-mid) 45%, var(--hero-dark) 100%);
  }
  .hero-photo::after { content: ""; position: absolute; inset: 0; background: rgba(20, 24, 28, 0.35); }
  .hero-content { position: relative; color: var(--white); }
  .hero-title { font-size: 40px; font-weight: 500; letter-spacing: 0.5px; }
  .hero-lead { font-size: 19px; margin-top: 6px; line-height: 1.35; }
  .explore-button {
    display: inline-block;
    margin-top: 26px;
    font-size: 14px;
    color: var(--brand-blue-deep);
    background: var(--white);
    padding: 7px 20px;
    border-radius: 2px;
    text-decoration: none;
  }

  .intro { flex: 1; display: flex; }
  .intro-text {
    width: 55%;
    background: var(--brand-blue);
    color: var(--white);
    padding: 54px 60px 0 110px;
  }
  .intro-kicker { font-size: 14px; opacity: 0.9; }
  .intro-title { font-size: 30px; font-weight: 500; margin-top: 4px; color: var(--white); }
  .intro-subtitle { font-size: 19px; font-weight: 500; color: var(--ink); margin-top: 20px; }
  .intro-body { font-size: 14px; line-height: 1.6; margin-top: 14px; max-width: 470px; }
  .intro-photo {
    flex: 1;
    background: linear-gradient(120deg, var(--wood-mid) 0%, var(--wood-dark) 100%);
  }
</style>
</head>
<body>
<div class="site">
  <header class="site-header">
    <a class="brand" href="#">
      <span class="brand-dot"></span>
      <span class="brand-name">Corvo Halden</span>
    </a>
    <nav class="main-nav">
      <a class="is-active" href="#">Home</a>
      <a href="#">About Us</a>
      <a href="#">What We Do</a>
      <a href="#">Products</a>
      <a href="#">Testimonials</a>
      <a href="#">Contact Us</a>
      <a class="demo-button" href="#">Request a Demo</a>
    </nav>
  </header>

  <section class="hero">
    <div class="hero-photo" role="img" aria-label="Photograph of a modern grey and white living room with a wall-mounted television"></div>
    <div class="hero-content">
      <h1 class="hero-title">Smart Device Integration</h1>
      <p class="hero-lead">We are focused on delivering affordable and easily usable<br>devices for your home and office!</p>
      <a class="explore-button" href="#">Explore More</a>
    </div>
  </section>

  <section class="intro">
    <div class="intro-text">
      <p class="intro-kicker">Welcome to</p>
      <h2 class="intro-title">Corvo Halden</h2>
      <h3 class="intro-subtitle">Our Aim</h3>
      <p class="intro-body">Our aim is to bring affordable smart home products to everyone, offering seamless integration and reliability. With a wide range of available cost options, outstanding service and experience, we are the solution for all your smart home technology solutions...</p>
    </div>
    <div class="intro-photo" role="img" aria-label="Photograph of a hand holding a smartphone running a smart home app beside a round smart door lock on dark wood"></div>
  </section>
</div>
</body>
</html>
```